Business card Pfotenweide

Business card is for a self-employed dog trainer with own dog school. Name and logo of the dog school are available. Color specifications as well. The design should be classy and minimalist, but also modern. An already existing idea would be: Front: Only the logo Back: Contact data

Font styles to use
Serif
Sans Serif
Other font styles liked:
• Trajan Pro

Colors
f78f20

Requirements
Must have
• Name: Marlene Kessel-Brand Title: Dipl. Dog Trainer Contain my logo Follow my font and color preferences (see files)

```html
<!DOCTYPE html>
<html lang="en">
<head>
<meta charset="utf-8">
<title>Pfotenweide business card</title>
<link rel="stylesheet" href="https://fonts.googleapis.com/css2?family=Cinzel:wght@400&family=Roboto+Condensed:wght@500&family=Roboto:wght@400;700&display=swap">
<style>
  :root {
    --backdrop: #2b2b2b;
    --card: #f1f1f0;
    --brown: #6f5f53;
    --grey-band: #9a9a9a;
    --text: #4a4a4a;
    --white: #ffffff;
  }
  * { margin: 0; padding: 0; box-sizing: border-box; }
  html, body { width: 1200px; height: 960px; overflow: hidden; }
  body { background: var(--backdrop); position: relative; font-family: "Roboto", sans-serif; }

  .card {
    position: absolute;
    width: 600px;
    height: 343px;
    background: var(--card);
    border-radius: 18px;
    overflow: hidden;
  }
  .card--front { left: 314px; top: 113px; }
  .card--back { left: 311px; top: 472px; }

  .band {
    position: absolute;
    left: 0; top: 37px;
    width: 600px; height: 110px;
    background: linear-gradient(90deg, var(--grey-band) 0, #8e8a86 90px, var(--brown) 130px, var(--brown) 100%);
  }
  .brand-dot {
    position: absolute;
    left: 101px; top: 35px;
    width: 116px; height: 116px;
    border-radius: 50%;
    background: var(--brown);
    border: 3px solid var(--white);
  }
  .brand-name {
    position: absolute;
    left: 0; width: 318px;
    top: 149px;
    text-align: center;
    font-family: "Cinzel", serif;
    font-size: 25px;
    color: var(--brown);
    letter-spacing: 1px;
  }
  .brand-url {
    position: absolute;
    left: 0; width: 318px;
    top: 176px;
    text-align: center;
    font-family: "Cinzel", serif;
    font-size: 7px;
    letter-spacing: 4px;
    color: var(--brown);
  }
  .holder {
    position: absolute;
    left: 358px; top: 71px;
    color: var(--white);
    font-family: "Roboto Condensed", sans-serif;
    font-weight: 500;
  }
  .holder__name { font-size: 21px; line-height: 24px; }
  .holder__title { font-size: 15px; line-height: 18px; }

  .contact {
    position: absolute;
    left: 358px; top: 208px;
    font-size: 14px;
    line-height: 18.5px;
    color: var(--text);
  }
  .contact__lines { margin-top: 8px; }
  .contact__key { font-weight: 700; color: var(--brown); display: inline-block; width: 14px; text-align: center; }

  .back-mark {
    position: absolute;
    left: 230px; top: 78px;
    width: 140px; height: 140px;
    border-radius: 50%;
    background: var(--brown);
  }
  .back-name {
    position: absolute;
    left: 0; width: 600px; top: 236px;
    text-align: center;
    font-family: "Cinzel", serif;
    font-size: 30px;
    letter-spacing: 1px;
    color: var(--brown);
  }
  .back-url {
    position: absolute;
    left: 0; width: 600px; top: 294px;
    text-align: center;
    font-family: "Cinzel", serif;
    font-size: 10px;
    letter-spacing: 6px;
    color: var(--brown);
  }
</style>
</head>
<body>
  <section class="card card--front" aria-label="Business card front">
    <div class="band"></div>
    <div class="brand-dot"></div>
    <div class="brand-name">PFOTENWEIDE</div>
    <div class="brand-url">WWW.PFOTENWEIDE.CH</div>
    <div class="holder">
      <div class="holder__name">Marlene Kessel-Brand</div>
      <div class="holder__title">Dipl. Dog Trainer</div>
    </div>
    <address class="contact" style="font-style: normal;">
      <div>142 Linden Court</div>
      <div>Brookfield, Oregon 97210</div>
      <div class="contact__lines">
        <div><span class="contact__key">P</span> : 541 208 3176</div>
        <div><span class="contact__key">E</span> : marlene@pfotenweide.ch</div>
        <div><span class="contact__key">W</span> : www.pfotenweide.ch</div>
      </div>
    </address>
  </section>

  <section class="card card--back" aria-label="Business card back">
    <div class="back-mark"></div>
    <div class="back-name">PFOTENWEIDE</div>
    <div class="back-url">WWW.PFOTENWEIDE.CH</div>
  </section>
</body>
</html>
```